Workbook Cover Design

I am needing the cover for a workbook designed. I have attached a sample cover along with a few images giving an idea what at I am looking for. I'm open to new color schemes. I also attached a flyer of the event to give you an idea of the current color theme. The workbook will be approximately 8.5 x 11.

Title : Fellowship Workshop 202
Lorna Tebbit Ministries

On the cover I would like to have four sections with the following title under each section:
Evangelism (use photo similar to hands with cross)
Praying in Tongues (Photo similar to bird with heart or one with a mouth speaking)
Authority of the Believer (Photo with badge or similar)
Healing (Photo of man and wheelchair or similar)

Using silhouettes are okay, but I prefer not to have any actual faces of people.

```html
<!DOCTYPE html>
<html lang="en">
<head>
<meta charset="utf-8">
<title>Fellowship Workshop 202 – Workbook Cover</title>
<link href="https://fonts.googleapis.com/css2?family=Great+Vibes&family=Montserrat:wght@400;500;900&display=swap" rel="stylesheet">
<style>
  :root {
    --stage: #d2d2d2;
    --paper: #f4f4f5;
    --navy: #0c1a5c;
    --navy-deep: #07104a;
    --gold: #c9a93a;
    --gold-light: #e2cb5c;
    --silver: #b4b6bb;
    --frame-line: #8d8d8f;
    --label-light: #dfe3f2;
  }
  * { box-sizing: border-box; margin: 0; padding: 0; }
  html, body { width: 1200px; height: 1000px; overflow: hidden; background: var(--stage); }
  body { position: relative; font-family: "Montserrat", sans-serif; }

  .cover {
    position: absolute; left: 210px; top: 30px; width: 780px; height: 940px;
    background: linear-gradient(160deg, #ffffff 0%, var(--paper) 40%, #e9e9eb 65%);
    overflow: hidden;
  }
  .band-silver {
    position: absolute; left: 0; right: 0; top: 619px; height: 20px;
    background: linear-gradient(90deg, #9fa1a6, #d4d5d8 50%, #9fa1a6);
  }
  .band-navy {
    position: absolute; left: 0; right: 0; top: 639px; bottom: 0;
    background: linear-gradient(160deg, var(--navy) 0%, var(--navy-deep) 45%, #0f2270 70%, var(--navy) 100%);
  }
  .frame {
    position: absolute; left: 40px; right: 40px; top: 49px; height: 840px;
    border: 1.5px solid var(--frame-line);
  }
  .ministry {
    position: absolute; top: 36px; left: 0; right: 0; text-align: center;
  }
  .ministry span {
    display: inline-block; padding: 0 10px 0 18px; background: #fbfbfb;
    font-size: 19px; font-weight: 500; letter-spacing: 10px; color: #6e6e70;
  }
  .title-script {
    position: absolute; top: 118px; left: 0; right: 0; text-align: center;
    font-family: "Great Vibes", cursive; font-size: 100px; line-height: 1;
    color: var(--gold);
    background: linear-gradient(90deg, var(--gold), var(--gold-light) 60%, var(--gold));
    -webkit-background-clip: text; background-clip: text; -webkit-text-fill-color: transparent;
    z-index: 2;
  }
  .title-main {
    position: absolute; top: 180px; left: 0; right: 0; text-align: center;
    font-weight: 900; font-size: 66px; letter-spacing: -1px; line-height: 1;
    color: var(--navy);
  }
  .subtitle {
    position: absolute; top: 262px; left: 0; right: 0; text-align: center;
    font-size: 25px; letter-spacing: 5px; color: var(--navy);
  }

  .tile {
    position: absolute; width: 205px; height: 216px; border-radius: 14px; padding: 5px;
    background: linear-gradient(135deg, #e7e8ea, var(--silver) 50%, #8c8e93);
  }
  .tile-art { width: 100%; height: 100%; border-radius: 10px; }
  .tile-evangelism { left: 187px; top: 318px; }
  .tile-healing { left: 406px; top: 318px; }
  .tile-authority { left: 187px; top: 555px; }
  .tile-tongues { left: 406px; top: 555px; }
  .art-evangelism { background: radial-gradient(circle at 50% 55%, #fff6d8 0%, #f0b860 30%, #9a6a40 65%, #6e6f7a 100%); }
  .art-healing { background: radial-gradient(circle at 70% 65%, #ffd27a 0%, #d77a2a 30%, #5b3a28 65%, #3a3230 100%); }
  .art-authority { background: radial-gradient(circle at 50% 50%, #e7c25c 0%, #c59a36 35%, #ffffff 62%); }
  .art-tongues { background: radial-gradient(circle at 50% 50%, #ff9a3a 0%, #b8361a 30%, #1a0d10 65%, #06070d 100%); }

  .label {
    position: absolute; width: 205px; text-align: center;
    font-size: 12.5px; letter-spacing: 2px; line-height: 17px;
  }
  .label-dark { color: var(--navy); top: 536px; }
  .label-light { color: var(--label-light); }
  .label-evangelism { left: 187px; }
  .label-healing { left: 406px; }
  .label-authority { left: 172px; width: 235px; top: 776px; }
  .label-tongues { left: 391px; width: 235px; top: 779px; }

  .author-tag {
    position: absolute; top: 840px; left: 0; right: 0; text-align: center;
    font-size: 20px; letter-spacing: 6px; color: #ffffff;
  }
  .author-name {
    position: absolute; top: 869px; left: 0; right: 0; text-align: center;
  }
  .author-name span {
    display: inline-block; padding: 0 12px 0 26px; background: #0b1963;
    font-size: 30px; font-weight: 500; letter-spacing: 16px; color: #ffffff; line-height: 38px;
  }
</style>
</head>
<body>
  <main class="cover">
    <div class="band-silver"></div>
    <div class="band-navy"></div>
    <div class="frame"></div>

    <p class="ministry"><span>LORNA TEBBIT MINISTRIES</span></p>

    <h1>
      <span class="title-script">Fellowship</span>
      <span class="title-main">WORKSHOP 202</span>
    </h1>
    <p class="subtitle">A LEARN AND DO CLINIC</p>

    <div class="tile tile-evangelism"><div class="tile-art art-evangelism" role="img" aria-label="Silhouetted open hands raised toward a glowing cross in a sunlit sky"></div></div>
    <div class="tile tile-healing"><div class="tile-art art-healing" role="img" aria-label="Silhouette of a man with arms raised beside an empty wheelchair at sunset"></div></div>
    <div class="tile tile-authority"><div class="tile-art art-authority" role="img" aria-label="Gold officer badge on a white background"></div></div>
    <div class="tile tile-tongues"><div class="tile-art art-tongues" role="img" aria-label="White dove flying through a heart made of fire on a dark background"></div></div>

    <p class="label label-dark label-evangelism">EVANGELISM</p>
    <p class="label label-dark label-healing">HEALING</p>
    <p class="label label-light label-authority">AUTHORITY OF THE<br>BELIEVER</p>
    <p class="label label-light label-tongues">PRAYING IN TONGUES</p>

    <p class="author-tag">AUTHOR</p>
    <p class="author-name"><span>LORNA TEBBIT</span></p>
  </main>
</body>
</html>
```